Web Design Project

To develop a web based Council Meeting Support system which includes 2 major components for each Council member:
1. Allow a council member to Vote on a motion during a council session
2. Allow a council member to flag notify the Chair their intention to speak on a motion
The application will have 3 separate interfaces:
Chair interface: Allows the Chair of the session to review voting and manage the speaker queue
Council interface: Allows each council member to vote on each motion and add flag their intention to speak for or against a motion
Admin interface: Allows administrators to initiate a session and import details on all meeting participants
We will begin by designing the Council Interface. (An example wireframe is attached) This council interface will give members the ability to request to speak, vote, view voting results and viewing the current motion number.
*** 4 Designs will be required overall. One for each interface and a login page ***
Needs to be designed so that it works well on an Tavlo or any tablet device.
Update: Looking for a brighter design, not a dark grey one. The blue colour from qarvel.example would be good.
- Request to Speak
Voting
Vote Results
Current Motion Number

```html
<!DOCTYPE html>
<html lang="en">
<head>
<meta charset="utf-8">
<title>Council Interface</title>
<link href="https://fonts.googleapis.com/css2?family=Arimo:wght@400;600&display=swap" rel="stylesheet">
<style>
:root{
  --navy:#0b3a6e;
  --blue-top:#0a63b8;
  --blue-bottom:#013a74;
  --soft-top:#6499cf;
  --soft-bottom:#3270ae;
  --btn-text:#dfe8f3;
  --text:#444;
  --rule:#1b3f66;
  --divider:#c9c9c9;
  --bg:#ffffff;
}
*{margin:0;padding:0;box-sizing:border-box}
html,body{width:1200px;height:1086px;overflow:hidden;background:var(--bg)}
body{position:relative;font-family:"Arimo",Arial,sans-serif;color:var(--text)}
.brand{position:absolute;left:34px;top:62px;display:flex;align-items:center;gap:14px}
.brand-mark{width:34px;height:34px;background:var(--navy)}
.brand-name{font-size:25px;font-weight:600;color:var(--navy)}
.motion-number{position:absolute;left:665px;top:80px;font-size:19px;color:#444}
.rule{position:absolute;left:29px;width:1142px;height:1px;background:var(--rule)}
.rule-top{top:169px}
.rule-mid{top:569px}
.speak-label{position:absolute;left:42px;top:199px;font-size:21px;color:var(--navy)}
.btn{position:absolute;display:flex;align-items:center;color:var(--btn-text);
  background:linear-gradient(var(--blue-top),var(--blue-bottom));border-radius:2px;
  box-shadow:0 1px 2px rgba(0,0,0,.25)}
.speak-btn{left:699px;width:424px;height:80px;padding-left:102px;font-size:21px}
.speak-for{top:224px}
.speak-against{top:328px}
.speak-remove{top:434px;background:linear-gradient(var(--soft-top),var(--soft-bottom))}
.panel{position:absolute;top:593px;height:403px;border:1px solid var(--navy)}
.panel-header{height:48px;padding-left:25px;display:flex;align-items:center;color:#fff;font-size:21px;
  background:linear-gradient(var(--blue-top),var(--blue-bottom))}
.voting{left:29px;width:443px}
.vote-btn{left:82px;width:233px;height:50px;padding-left:71px;font-size:21px}
.vote-for{top:121px}
.vote-against{top:202px}
.vote-abstain{top:280px}
.results{left:520px;width:648px}
.col{position:absolute;top:66px}
.col-for{left:37px}
.col-against{left:232px}
.col-abstain{left:465px}
.col-title{font-size:18px;color:var(--navy);text-decoration:underline;margin-bottom:9px;display:inline-block}
.col ul{list-style:none}
.col li{font-size:14.5px;height:25px;line-height:25px;color:#555;display:flex}
.col li span{width:41px}
.col-divider{position:absolute;top:72px;width:1px;height:320px;background:var(--divider)}
.d1{left:208px}
.d2{left:444px}
</style>
</head>
<body>
<div class="brand"><div class="brand-mark"></div><span class="brand-name">Northfield Engineers Council</span></div>
<div class="motion-number">Current Motion # :</div>
<div class="rule rule-top"></div>

<div class="speak-label">I Would Like to Speak :</div>
<div class="btn speak-btn speak-for">For Motion</div>
<div class="btn speak-btn speak-against">Against Motion</div>
<div class="btn speak-btn speak-remove">Remove From Queue</div>

<div class="rule rule-mid"></div>

<section class="panel voting">
  <div class="panel-header">Voting</div>
  <div class="btn vote-btn vote-for">For</div>
  <div class="btn vote-btn vote-against">Against</div>
  <div class="btn vote-btn vote-abstain">Abstain</div>
</section>

<section class="panel results">
  <div class="panel-header">Vote Results</div>
  <div class="col col-for">
    <div class="col-title">FOR</div>
    <ul>
      <li><span>A.</span>Marchand</li><li><span>S.</span>Veldt</li><li><span>P.</span>Corrigan</li>
      <li><span>I.</span>Mehra</li><li><span>T.</span>Lam</li><li><span>R.</span>A Dunmore</li>
      <li><span>S.</span>K. Rao</li><li><span>S.</span>Veldt</li><li><span>L.</span>Hale</li>
      <li><span>B.</span>Varga</li>
    </ul>
  </div>
  <div class="col-divider d1"></div>
  <div class="col col-against">
    <div class="col-title">AGAINST&nbsp;</div>
    <ul>
      <li><span>A.</span>Marchand</li><li><span>S.</span>Veldt</li><li><span>P.</span>Corrigan</li>
      <li><span>I.</span>Mehra</li><li><span>T.</span>Lam</li><li><span>R.</span>A Dunmore</li>
      <li><span>S.</span>K. Rao</li><li><span>S.</span>Veldt</li><li><span>L.</span>Hale</li>
      <li><span>B.</span>Varga</li><li><span>C.</span>D Pell</li><li><span>T.</span>Joshi</li>
    </ul>
  </div>
  <div class="col-divider d2"></div>
  <div class="col col-abstain">
    <div class="col-title">ABSTAIN</div>
    <ul>
      <li><span>A.</span>Marchand</li><li><span>S.</span>Veldt</li><li><span>P.</span>Corrigan</li>
      <li><span>I.</span>Mehra</li><li><span>T.</span>Lam</li>
    </ul>
  </div>
</section>
</body>
</html>
```